Design a Flyer/Poster for "VELVET HARBOUR" Theme Event

Hi guys,

THIS IS QUITE URGENT - we need to go to print ASAP...

We're after a funky VELVET HARBOUR flyer/poster for a Restaurant/Bar's 2nd Birthday event we're running next month.

STYLE: Velvet Harbour Theme
IDEAS: camels, tents, rugs, street food, candles, red lights, belly dancers, etc

CONTENT:
(MUST HAVE)

M-LOFT's 2nd Birthday
VELVET HARBOUR
3rd July
from 8:30pm until Midnight
RSVP today at RSVP@mloftdeli.com.au

LOGO: Attached - please use within the design

CO WEBSITE: www.portelino.com.au

ADDITIONAL INSPIRATION:
Google "Velvet Harbour" - there's plenty there to be inspired... just make sure it's current (2015).

Any Q's just ask.

Cheers guys!

Regards,
GUS :)

```html
<!DOCTYPE html>
<html lang="en">
<head>
<meta charset="utf-8">
<title>M-LOFT's 2nd Birthday – Velvet Harbour</title>
<link href="https://fonts.googleapis.com/css2?family=Cinzel:wght@500;600;700&display=swap" rel="stylesheet">
<style>
  :root {
    --night-deep: #05071a;
    --night-mid: #0d1540;
    --night-glow: #1f3f8f;
    --arch-red: #7a1418;
    --arch-red-deep: #3a0a10;
    --gold: #e2c27a;
    --gold-light: #f6e2a8;
    --gold-dark: #a9853e;
    --cream: #f3e6c4;
  }
  * { margin: 0; padding: 0; box-sizing: border-box; }
  html, body { width: 846px; height: 1200px; overflow: hidden; background: var(--night-deep); }
  .poster {
    position: relative;
    width: 846px;
    height: 1200px;
    overflow: hidden;
    font-family: "Cinzel", "Times New Roman", serif;
    color: var(--gold);
    background:
      radial-gradient(ellipse 320px 520px at 820px 640px, rgba(31,63,143,0.75), transparent 70%),
      radial-gradient(ellipse 260px 420px at 20px 700px, rgba(31,63,143,0.55), transparent 70%),
      linear-gradient(180deg, var(--night-deep) 0%, var(--night-mid) 55%, var(--night-deep) 100%);
  }
  .stars { position: absolute; inset: 0; width: 846px; height: 1200px; }
  .corner-pattern {
    position: absolute;
    top: -120px;
    width: 420px;
    height: 420px;
    border-radius: 50%;
    background: radial-gradient(circle, rgba(169,133,62,0.35), rgba(169,133,62,0.12) 60%, transparent 72%);
  }
  .corner-pattern--left { left: -120px; }
  .corner-pattern--right { right: -120px; }
  .arch { position: absolute; inset: 0; width: 846px; height: 1200px; }
  .arch-pattern {
    position: absolute;
    left: 150px; top: 300px;
    width: 546px; height: 420px;
    border-radius: 50%;
    background: radial-gradient(circle, rgba(160,40,40,0.35), transparent 70%);
  }
  .dancer-area {
    position: absolute;
    top: 620px;
    width: 190px;
    height: 340px;
    background: radial-gradient(ellipse, rgba(30,6,10,0.28), transparent 70%);
  }
  .dancer-area--left { left: 90px; }
  .dancer-area--right { right: 90px; }
  .bottom-pattern {
    position: absolute;
    left: 220px; top: 1040px;
    width: 406px; height: 160px;
    border-radius: 50% 50% 0 0;
    background: radial-gradient(ellipse at 50% 100%, rgba(150,50,40,0.35), transparent 70%);
  }
  .brand {
    position: absolute;
    top: 30px; left: 0; width: 100%;
    text-align: center;
    font-size: 26px;
    font-weight: 600;
    letter-spacing: 3px;
    color: var(--gold);
  }
  .line {
    position: absolute;
    left: 0; width: 100%;
    text-align: center;
    white-space: nowrap;
    color: var(--gold);
    text-shadow: 0 2px 4px rgba(0,0,0,0.55);
  }
  .host { top: 305px; font-size: 60px; font-weight: 600; color: var(--gold-light); }
  .occasion { top: 378px; font-size: 30px; font-weight: 600; }
  .flourish {
    position: absolute;
    left: 313px;
    width: 220px; height: 22px;
    border-radius: 11px;
    background: linear-gradient(90deg, transparent, rgba(226,194,122,0.55), transparent);
  }
  .flourish--top { top: 475px; }
  .flourish--bottom { top: 618px; }
  .event-title { top: 516px; font-size: 60px; font-weight: 700; color: var(--gold-light); letter-spacing: 1px; }
  .date { top: 722px; font-size: 38px; font-weight: 600; }
  .time { top: 790px; font-size: 38px; font-weight: 600; }
  .time-end { top: 840px; font-size: 38px; font-weight: 600; }
  .rsvp { top: 905px; font-size: 24px; font-weight: 600; color: var(--cream); }
  .emblem {
    position: absolute;
    left: 403px; top: 995px;
    width: 40px; height: 58px;
    border-radius: 50%;
    background: radial-gradient(ellipse, rgba(226,194,122,0.6), transparent 70%);
  }
  .website { top: 1143px; font-size: 22px; font-weight: 600; color: var(--cream); letter-spacing: 1px; }
</style>
</head>
<body>
<div class="poster">
  <svg class="stars" viewBox="0 0 846 1200" aria-hidden="true">
    <g fill="#ffffff">
      <circle cx="40" cy="520" r="1.2" opacity="0.8"/>
      <circle cx="22" cy="640" r="1" opacity="0.6"/>
      <circle cx="60" cy="860" r="1.3" opacity="0.7"/>
      <circle cx="18" cy="1000" r="1" opacity="0.5"/>
      <circle cx="810" cy="480" r="1.2" opacity="0.8"/>
      <circle cx="830" cy="720" r="1.4" opacity="0.7"/>
      <circle cx="800" cy="940" r="1" opacity="0.6"/>
      <circle cx="822" cy="1080" r="1.2" opacity="0.5"/>
      <circle cx="120" cy="300" r="1" opacity="0.6"/>
      <circle cx="730" cy="280" r="1" opacity="0.6"/>
      <circle cx="260" cy="180" r="1.1" opacity="0.5"/>
      <circle cx="590" cy="160" r="1.1" opacity="0.5"/>
      <circle cx="380" cy="1190" r="1" opacity="0.5"/>
    </g>
  </svg>

  <div class="corner-pattern corner-pattern--left" role="img" aria-label="Gold mandala pattern in the top left corner"></div>
  <div class="corner-pattern corner-pattern--right" role="img" aria-label="Gold mandala pattern in the top right corner"></div>

  <svg class="arch" viewBox="0 0 846 1200" aria-hidden="true">
    <defs>
      <linearGradient id="archFill" x1="0" y1="0" x2="0" y2="1">
        <stop offset="0" stop-color="#8a1a1c"/>
        <stop offset="0.55" stop-color="#6e1218"/>
        <stop offset="1" stop-color="#2e0810"/>
      </linearGradient>
      <linearGradient id="archGold" x1="0" y1="0" x2="1" y2="1">
        <stop offset="0" stop-color="#f6e2a8"/>
        <stop offset="0.5" stop-color="#c9a258"/>
        <stop offset="1" stop-color="#f0d58e"/>
      </linearGradient>
    </defs>
    <path d="M51,1200 V440 C51,410 80,392 120,388 C150,386 160,372 160,355 C210,348 255,318 300,282 C360,236 405,214 423,180 C441,214 486,236 546,282 C591,318 636,348 686,355 C686,372 696,386 726,388 C766,392 795,410 795,440 V1200 Z"
          fill="url(#archFill)" stroke="url(#archGold)" stroke-width="9"/>
    <path d="M64,1200 V446 C64,420 88,404 122,401 C158,398 172,382 173,367 C222,358 265,330 309,294 C366,248 406,228 423,202 C440,228 480,248 537,294 C581,330 624,358 673,367 C674,382 688,398 724,401 C758,404 782,420 782,446 V1200"
          fill="none" stroke="#c9a258" stroke-width="1.5" opacity="0.7"/>
  </svg>

  <div class="arch-pattern" role="img" aria-label="Faint red mandala pattern inside the arch"></div>
  <div class="dancer-area dancer-area--left" role="img" aria-label="Faint silhouette of a belly dancer"></div>
  <div class="dancer-area dancer-area--right" role="img" aria-label="Faint silhouette of a belly dancer"></div>
  <div class="bottom-pattern" role="img" aria-label="Faint mandala pattern at the foot of the arch"></div>

  <div class="brand">M-LOFT</div>

  <div class="line host">M-LOFT's</div>
  <div class="line occasion">2nd Birthday</div>
  <div class="flourish flourish--top" role="img" aria-label="Gold scroll ornament"></div>
  <div class="line event-title">VELVET HARBOUR</div>
  <div class="flourish flourish--bottom" role="img" aria-label="Gold scroll ornament"></div>

  <div class="line date">3rd July</div>
  <div class="line time">From 8:30pm</div>
  <div class="line time-end">till Midnight</div>
  <div class="line rsvp">RSVP today at RSVP@mloftdeli.com.au</div>

  <div class="emblem" role="img" aria-label="Small gold ornamental emblem"></div>

  <div class="line website">www.portelino.com.au</div>
</div>
</body>
</html>
```